Redesign our business card for more impact

We want to completely replace the back design of our card, and refresh or even change the front entirely. We are happy with our black K4 logo and do not want to change it.
Our company address changed too. It is now 2307 Larkmoor, Irvine, CA 92741
Updates

It was reported by Art Harbor email today that the uploaded files didnt upload. I am trying again.

Target Market(s)

Architects and Building Owners (People making multi-million dollar decisions)

Industry/Entity Type

Consulting Engineering

Contact Information for Business Card

Contact info on the front. "wallpaper" design on back with tag line on the back "Engineering Your Future"

Font styles to use
Sans Serif

Requirements
Must have
• A vivid, modern, impactful ...but tasteful back of card design. It should communicate our premier status, but grab attention as innovative. DESIGN SHOULD BE ELEGANT AND NOT TOO BUSY.
Nice to have
• Repeating pattern, multi-color, something creative...
Should not have
• Anything that looks too playful or that we are not serious professionals. It should also not be too boring or conservative.

```html
<!DOCTYPE html>
<html lang="en">
<head>
<meta charset="utf-8">
<title>K4 Engineering – Business Card</title>
<link rel="stylesheet" href="https://fonts.googleapis.com/css2?family=Lato:wght@400;700;900&display=swap">
<style>
  :root {
    --stage: #2b2d31;
    --ink: #000000;
    --paper: #ffffff;
    --accent-blue: #2a8fd8;
    --accent-magenta: #a0288f;
    --badge-dark: #2e2e30;
    --badge-ring: #5b5b60;
    --warm-red: #f0344f;
    --warm-orange: #f7873a;
    --violet: #7a2fae;
    --sky: #2aa3e6;
    --deep-blue: #1f6fc7;
  }
  * { box-sizing: border-box; margin: 0; padding: 0; }
  html, body { width: 1200px; height: 900px; overflow: hidden; }
  body {
    background: var(--stage);
    font-family: "Lato", sans-serif;
    display: flex;
    align-items: center;
    justify-content: center;
    gap: 40px;
  }
  .card {
    position: relative;
    width: 540px;
    height: 309px;
    border-radius: 22px;
    overflow: hidden;
  }
  .card-wallpaper {
    position: absolute;
    inset: 0;
    background:
      radial-gradient(circle at 18% 8%, var(--warm-orange) 0%, transparent 28%),
      radial-gradient(circle at 30% 15%, var(--warm-red) 0%, transparent 38%),
      radial-gradient(circle at 72% 18%, #ffffff 0%, transparent 40%),
      radial-gradient(circle at 85% 70%, var(--sky) 0%, transparent 45%),
      linear-gradient(135deg, #e0369a 0%, var(--violet) 40%, #4d54c8 62%, var(--deep-blue) 100%);
  }

  /* Front */
  .front-panel {
    position: absolute;
    top: 22px; left: 24px; right: 24px; bottom: 22px;
    background: var(--ink);
    color: var(--paper);
    padding: 24px 30px;
    overflow: hidden;
  }
  .wordmark {
    font-weight: 900;
    font-size: 58px;
    line-height: 1;
    letter-spacing: 1px;
    color: var(--paper);
  }
  .contact-block {
    position: absolute;
    left: 150px;
    top: 66px;
  }
  .person-name {
    color: var(--accent-blue);
    font-size: 22px;
    line-height: 1.2;
    font-weight: 400;
    letter-spacing: 0.5px;
  }
  .person-title {
    font-size: 13px;
    line-height: 1.3;
    margin-top: 3px;
    margin-bottom: 9px;
  }
  .contact-list { list-style: none; }
  .contact-item {
    display: flex;
    align-items: flex-start;
    gap: 8px;
    font-size: 13px;
    line-height: 1.3;
    margin-bottom: 4px;
  }
  .contact-item:last-child { margin-bottom: 0; }
  .contact-icon {
    flex: none;
    width: 15px; height: 15px;
    background: var(--accent-magenta);
    display: flex; align-items: center; justify-content: center;
    margin-top: 1px;
  }

  /* Back */
  .tagline-badge {
    position: absolute;
    left: 170px; top: 52px;
    width: 200px; height: 200px;
    border-radius: 50%;
    background: var(--badge-dark);
    border: 8px solid var(--badge-ring);
    display: flex;
    flex-direction: column;
    align-items: center;
    justify-content: center;
    color: var(--paper);
  }
  .tagline-badge .wordmark { font-size: 60px; }
  .tagline {
    font-size: 19px;
    font-weight: 700;
    text-align: center;
    line-height: 1.15;
    margin-top: 8px;
  }
</style>
</head>
<body>

  <section class="card card-front">
    <div class="card-wallpaper" role="img" aria-label="Multicolour faceted crystal pattern in red, magenta, violet and blue"></div>
    <div class="front-panel">
      <div class="wordmark">K4</div>
      <div class="contact-block">
        <h1 class="person-name">DANA WHITLOCK</h1>
        <p class="person-title">PEHFDP, LEED<br>APCEO/Principal</p>
        <ul class="contact-list">
          <li class="contact-item">
            <span class="contact-icon"><svg width="10" height="10" viewBox="0 0 10 10"><path d="M2 1 L4 1 L4.6 3 L3.5 3.8 Q4.5 5.8 6.2 6.5 L7 5.4 L9 6 L9 8 Q5 9 2.5 6 Q1 4 2 1Z" fill="#fff"/></svg></span>
            (949) 555-0174
          </li>
          <li class="contact-item">
            <span class="contact-icon"><svg width="10" height="8" viewBox="0 0 10 8"><rect x="0.5" y="0.5" width="9" height="7" fill="none" stroke="#fff"/><path d="M0.5 0.5 L5 4.5 L9.5 0.5" fill="none" stroke="#fff"/></svg></span>
            dana.whitlock@k4eng.com
          </li>
          <li class="contact-item">
            <span class="contact-icon"><svg width="10" height="10" viewBox="0 0 10 10"><circle cx="5" cy="5" r="4.2" fill="none" stroke="#fff"/><ellipse cx="5" cy="5" rx="1.8" ry="4.2" fill="none" stroke="#fff"/><path d="M0.8 5 H9.2" stroke="#fff"/></svg></span>
            k4eng.com
          </li>
          <li class="contact-item">
            <span class="contact-icon"><svg width="8" height="10" viewBox="0 0 8 10"><path d="M4 10 L0.8 5 A3.5 3.5 0 1 1 7.2 5 Z" fill="#fff"/><circle cx="4" cy="3.6" r="1.3" fill="#a0288f"/></svg></span>
            2307 Larkmoor, Irvine,<br>CA 92741
          </li>
        </ul>
      </div>
    </div>
  </section>

  <section class="card card-back">
    <div class="card-wallpaper" role="img" aria-label="Multicolour faceted crystal wallpaper pattern in red, magenta, violet, white and blue"></div>
    <div class="tagline-badge">
      <div class="wordmark">K4</div>
      <p class="tagline">Engineering<br>Your Future</p>
    </div>
  </section>

</body>
</html>
```